Business Card for a Floral & Decorating Business

I would like to take my current logo and create a better business card. I am looking for elegance as I am a florist and event decorator. My logo has multiple colour options. I like colours like green, purple, pink and orange, I think I would like a white card, open to black back ground. I want it to feel elegant and romantic. I like metallic lettering that maybe is indented in the paper, I also like glossy paper. I have a full logo already as well as a badge. I have attached both in multiple colours.m
Updates

Need extra days to review

Target Market(s)

Weddings, special events, floral customers

Industry/Entity Type

Floral and decorating

Contact Information for Business Card

Phone number, email, instagram, facebook, title, name, logo

Font styles to use
Script

Requirements
Nice to have
• Elegant

```html
<!DOCTYPE html>
<html lang="en">
<head>
<meta charset="utf-8">
<title>Maren Holloway business card</title>
<link rel="stylesheet" href="https://fonts.googleapis.com/css2?family=Lato:wght@400;700&family=Cormorant+Garamond:wght@500&display=swap">
<style>
  :root {
    --backdrop: #e9e9e7;
    --card: #333333;
    --rose: #e9a58f;
    --ink-light: #f2f2f2;
    --rule: #cfcfcf;
    --shade-dark: #3d3d3d;
    --shade-light: #8a8a8a;
  }
  * { margin: 0; padding: 0; box-sizing: border-box; }
  html, body { width: 1200px; height: 802px; overflow: hidden; background: var(--backdrop); }
  .stage {
    position: relative; width: 1200px; height: 802px;
    display: flex; align-items: center; justify-content: center; gap: 48px;
  }
  .card {
    position: relative; width: 520px; height: 298px;
    background: var(--card);
    box-shadow: 0 6px 18px rgba(0,0,0,0.22);
  }
  /* front */
  .brand-block {
    position: absolute; left: 28px; top: 0; width: 230px; height: 100%;
    display: flex; flex-direction: column; align-items: center; justify-content: center; gap: 8px;
  }
  .brand-mark { width: 22px; height: 22px; border-radius: 50%; background: var(--rose); }
  .brand-name {
    font-family: "Lato", sans-serif; font-weight: 400; font-size: 26px;
    color: var(--rose); letter-spacing: 1px;
  }
  .brand-tagline {
    font-family: "Cormorant Garamond", serif; font-weight: 500; font-size: 10px;
    letter-spacing: 2.5px; color: var(--rose);
  }
  .divider {
    position: absolute; left: 282px; top: 96px; width: 2px; height: 112px; background: var(--rule);
  }
  .contact {
    position: absolute; left: 302px; top: 92px;
    font-family: "Lato", sans-serif; color: var(--ink-light);
  }
  .contact-name { font-weight: 700; font-size: 15px; color: var(--rose); letter-spacing: 0.5px; }
  .contact-title { font-size: 13px; margin-bottom: 6px; }
  .contact-row { display: flex; align-items: center; gap: 8px; font-size: 13px; line-height: 19px; }
  .contact-row svg { width: 12px; height: 12px; flex: none; }
  /* back */
  .floral-art {
    position: absolute; left: 36px; top: 30px; width: 200px; height: 238px;
    background: radial-gradient(ellipse at 55% 55%, var(--shade-light) 0%, var(--shade-dark) 70%, var(--card) 100%);
    opacity: 0.55; border-radius: 6px;
  }
  .back .brand-block { left: 250px; width: 250px; align-items: center; }
  .back .brand-name { font-size: 27px; }
</style>
</head>
<body>
<main class="stage">
  <section class="card front">
    <div class="brand-block">
      <span class="brand-mark"></span>
      <span class="brand-name">Maren Holloway</span>
      <span class="brand-tagline">DECORATING &amp; FLORALS.</span>
    </div>
    <div class="divider"></div>
    <div class="contact">
      <p class="contact-name">ELLIOT MARSH</p>
      <p class="contact-title">Manager</p>
      <p class="contact-row">
        <svg viewBox="0 0 12 12"><rect width="12" height="12" rx="2" fill="var(--rose)"/><path d="M3 4c0 3 2 5 5 5l1-1.5-1.5-1-1 .8c-1-.4-1.6-1-2-2l.8-1L4.5 3z" fill="var(--card)"/></svg>
        555-014-7720
      </p>
      <p class="contact-row">
        <svg viewBox="0 0 12 12"><rect width="12" height="12" rx="2" fill="var(--rose)"/><rect x="2.5" y="3.5" width="7" height="5" fill="none" stroke="var(--card)" stroke-width="1"/><path d="M2.5 3.5 6 6.5 9.5 3.5" fill="none" stroke="var(--card)" stroke-width="1"/></svg>
        hello@marenholloway.com
      </p>
      <p class="contact-row">
        <svg viewBox="0 0 12 12"><rect width="12" height="12" rx="2" fill="var(--rose)"/></svg>
        #marenhollowayflorals
      </p>
      <p class="contact-row">
        <svg viewBox="0 0 12 12"><circle cx="6" cy="6" r="6" fill="var(--rose)"/></svg>
        #marenhollowayflorals
      </p>
    </div>
  </section>

  <section class="card back">
    <div class="floral-art" role="img" aria-label="Embossed floral illustration in soft grey"></div>
    <div class="brand-block">
      <span class="brand-name">Maren Holloway</span>
      <span class="brand-tagline">DECORATING &amp; FLORALS.</span>
    </div>
  </section>
</main>
</body>
</html>
```